Consulting Engineering Firm WordPress Design

We need:
1. A WordPress design.
2. Company is based in Sydney, Australia.
3. Company name: K7R Consulting Engineers.
The company provide professional engineering consultancy services to building owners, operators, developers and designers.
4. Overall purpose or objective of the website: The website must reflect high professionalism. It will provide information to our clients on who we are, what we do, how we do, our experience, projects we have done in the past and contact information.
5. Company logo is in the uploaded files.
6. Webpage:
6.1. Standard Web pages. Not for e-commercial.
6.2. Use WordPress. Website will be hosted on Hostvane WordPress hosting.
7. Coding required.
8. The winning designer (Winner) shall assist to host the wordpress design on Hostvane WordPress hosting services. Winner will transfer the files and configure to make sure all pages, links, posts and blogs works as intended.
8. We would like the site to have the same theme as the company brochure which is uploaded here.
9. The SSL certificate must be configured in the coded WordPress.
10. Pages:
i. Home - will have images updating every 4 s. Refer to company brochure for the images I am after. Use similar or better high quality images.
ii. About Us
iii. Services - This will have sub pages.
iv. Markets- This will have sub pages.
v. Projects- This will have sub pages.
vi. Contact - This will have company contact details. Also, it will request first name, last name, phone number, email address, comments and submit button.
11. I want a clean, minimalist websites that has a more professional tone. Please do not use too much unnecessary graphical elements and avoid loud vibrant colours.
12. Use images related to technology, buildings, smart city, smart buildings, energy savings, control system, energy dash boards, etc.
Target Market(s)
Building services engineering consultants, builders, building owners, building managers.

```html
<!DOCTYPE html>
<html lang="en">
<head>
<meta charset="utf-8">
<title>K7R Consulting Engineers – Building Management System</title>
<link href="https://fonts.googleapis.com/css2?family=Lato:ital,wght@0,300;0,400;0,700;0,900;1,400&display=swap" rel="stylesheet">
<style>
:root{
  --blue:#0c3c9e;
  --blue-deep:#082c7a;
  --blue-dark:#1d2f86;
  --charcoal:#3b3b3d;
  --ink:#222;
  --text:#555;
  --line:#c9ced8;
  --white:#fff;
}
*{margin:0;padding:0;box-sizing:border-box}
html,body{width:1200px;height:4680px;overflow:hidden}
body{font-family:'Lato',Arial,sans-serif;color:var(--ink);background:var(--white);position:relative}
.abs{position:absolute}
.btn{display:inline-block;background:var(--blue);color:var(--white);font-size:12px;font-weight:700;letter-spacing:.5px;text-transform:uppercase;text-align:center}

/* header */
.header{top:0;left:0;width:1200px;height:110px;background:var(--white)}
.topbar{left:400px;top:0;width:800px;height:55px}
.logo{left:148px;top:18px;display:flex;align-items:center;gap:10px}
.logo-mark{width:54px;height:54px;border:4px solid var(--blue);border-radius:50%}
.logo-name{font-size:18px;font-weight:900;color:var(--blue);line-height:1.05}
.logo-name small{display:block;font-size:10px;font-weight:900;letter-spacing:.3px}
.contact-top{top:14px;color:var(--white);font-size:12px;display:flex;align-items:center;gap:8px}
.quote-top{left:918px;top:8px;width:132px;height:38px;line-height:38px}
.nav{top:78px;left:497px;font-size:12px;color:#444}
.nav span{position:absolute;white-space:nowrap}

/* hero */
.hero-photo{top:110px;left:0;width:1200px;height:670px;
  background:
    radial-gradient(ellipse 420px 520px at 870px 260px, rgba(200,210,222,.55), rgba(200,210,222,0) 70%),
    radial-gradient(ellipse 260px 600px at 1120px 200px, rgba(150,160,172,.55), rgba(150,160,172,0) 70%),
    linear-gradient(115deg,#1f2227 0%,#33363c 35%,#4b4f57 60%,#6f7680 100%)}
.hero-edge{left:0;top:110px}
.hero-title{left:148px;top:332px;border-left:4px solid var(--white);padding-left:20px;color:var(--white);font-size:37px;font-weight:900;line-height:1.28}
.hero-sub{left:148px;top:430px;color:var(--white);font-size:30px;font-weight:400}
.hero-btn{left:148px;top:493px;width:135px;height:38px;line-height:38px}

/* about */
.about-photo{left:148px;top:862px;width:400px;height:420px}
.about-text{left:600px;top:890px;width:450px}
.section-title{font-size:29px;font-weight:300;letter-spacing:.3px;text-transform:uppercase}
.section-title b{font-weight:900}
.about-name{margin-top:32px;color:var(--blue);font-weight:700;font-size:18px;line-height:1.5}
.about-body{margin-top:22px;font-size:12.4px;line-height:22.5px;color:var(--text)}
.about-btn{margin-top:28px;width:135px;height:40px;line-height:40px}

/* services band */
.band-title{color:var(--white);font-size:29px;font-weight:900}
.ticks{list-style:none;color:var(--white);font-size:12.6px}
.ticks li{position:relative;padding-left:34px;height:27px;line-height:27px;white-space:nowrap}
.ticks li::before{content:"";position:absolute;left:4px;top:8px;width:11px;height:11px;border:2px solid var(--white);border-radius:50%}
.diligent{color:var(--white);font-size:18px;font-weight:900}
.phase-title{left:0;width:1200px;top:1792px;text-align:center;color:var(--white);font-size:29px;font-weight:900}
.phase-diagram{left:170px;top:1880px;width:880px;height:190px;border-radius:95px;
  background:linear-gradient(90deg,rgba(12,60,158,.55),rgba(60,96,170,.45) 50%,rgba(12,60,158,.55))}

/* assets */
.assets-head{top:2255px;left:0;width:1200px;text-align:center}
.assets-sub{margin-top:12px;font-size:12.5px;color:#444}
.asset{width:152px;height:152px;border:2px solid var(--blue);border-radius:50%;display:flex;flex-direction:column;align-items:center;justify-content:center;text-align:center;font-size:12.5px;color:#444;line-height:1.3}
.asset svg{margin-bottom:8px}

/* why */
.why-text{left:622px;top:2988px;width:430px}
.why-text .section-title{color:var(--white)}
.why-list{margin-top:20px;list-style:none;color:var(--white);font-size:12.4px;line-height:27px}
.why-list li{position:relative;padding-left:18px}
.why-list li::before{content:"";position:absolute;left:0;top:8px;width:9px;height:9px;border:2px solid var(--white);border-radius:50%}

/* contact */
.contact-head{top:3612px;left:0;width:1200px;text-align:center}
.field{border:1.5px solid var(--line);background:var(--white);font-size:12px;font-style:italic;color:#9aa0aa;padding:18px 16px}
.send{left:535px;top:3999px;width:135px;height:40px;line-height:40px}

/* footer */
.footer{top:4240px;left:0;width:1200px;height:400px;background:var(--blue)}
.foot-about{left:148px;top:4436px;width:420px;color:var(--white);font-size:12.4px;line-height:23px}
.foot-more{display:block;margin-top:16px;text-decoration:underline}
.foot-h{color:var(--white);font-size:22px;font-weight:300}
.foot-h b{font-weight:900}
.foot-links{list-style:none;color:var(--white);font-size:12px;line-height:27px}
.foot-contact{color:var(--white);font-size:12px;line-height:29px}
.foot-contact div{display:flex;align-items:center;gap:8px}
.socials{display:flex;gap:15px}
.socials span{width:34px;height:34px;border:2px solid var(--white);border-radius:50%;display:block}
.bottom{top:4640px;left:0;width:1200px;height:40px;background:var(--blue-dark);color:var(--white);font-size:11px}
</style>
</head>
<body>

<!-- Header -->
<header class="header abs">
  <svg class="topbar abs" width="800" height="55" viewBox="0 0 800 55"><polygon points="25,0 800,0 800,55 25,55 0,0" fill="#0c3c9e"/><line x1="247" y1="12" x2="247" y2="42" stroke="#fff" stroke-width="1"/></svg>
  <div class="logo abs"><span class="logo-mark"></span><span class="logo-name">K7R<small>CONSULTING ENGINEERS</small></span></div>
  <div class="contact-top abs" style="left:463px">
    <svg width="26" height="26" viewBox="0 0 26 26"><circle cx="13" cy="13" r="11.5" fill="none" stroke="#fff" stroke-width="1.8"/><path d="M9 8c1-1 2 0 2.5 1.5s-1 1.5-.5 3 2 3 3.5 3.5 1.5-1 3-.5 2.5 1.5 1.5 2.5c-2 2-5 0-7-2s-4-5-3-8z" fill="#fff"/></svg>
    PHONE: 0198 765 432</div>
  <div class="contact-top abs" style="left:662px">
    <svg width="26" height="26" viewBox="0 0 26 26"><circle cx="13" cy="13" r="11.5" fill="none" stroke="#fff" stroke-width="1.8"/><rect x="7" y="9" width="12" height="8.5" fill="none" stroke="#fff" stroke-width="1.6"/><path d="M7 9l6 5 6-5" fill="none" stroke="#fff" stroke-width="1.6"/></svg>
    E-MAIL: info@k7rmail.com</div>
  <div class="btn quote-top abs" style="background:var(--blue-deep)">Get a quote</div>
  <nav class="nav abs">
    <span style="left:0">HOME</span><span style="left:81px">ABOUT US</span><span style="left:188px">SERVICES</span><span style="left:287px">MARKETS</span><span style="left:388px">PROJECTS</span><span style="left:491px">CONTACT</span>
  </nav>
</header>

<!-- Hero -->
<section class="hero">
  <div class="hero-photo abs" role="img" aria-label="Photo looking up at glass office towers against a pale sky"></div>
  <svg class="hero-edge abs" width="1200" height="670" viewBox="0 0 1200 670">
    <polygon points="0,605 200,605 600,635 0,670" fill="#0c3c9e"/>
    <polygon points="0,660 590,635 1200,660 1200,670 0,670" fill="#fff"/>
  </svg>
  <h1 class="hero-title abs">BUILDING MANAGEMENT<br>SYSTEM (BMS)</h1>
  <p class="hero-sub abs">Capability Statement</p>
  <div class="btn hero-btn abs">Get a quote</div>
</section>

<!-- About -->
<section class="about">
  <svg class="about-photo abs" viewBox="0 0 400 420">
    <circle cx="195" cy="210" r="188" fill="#e9ebef" role="img" aria-label="Portrait photo of the principal engineer"/>
    <path d="M395 240 A206 206 0 1 1 330 60" fill="none" stroke="#0c3c9e" stroke-width="9"/>
  </svg>
  <div class="about-text abs">
    <h2 class="section-title">About <b>Us</b></h2>
    <p class="about-name">D.KESTRAN<br>MIEAust CPEng NER APEC Engineer IntPE(Aus)</p>
    <p class="about-body">K7R Consulting Engineers is an accomplished registered professional engineer with over seventeen (17) years extensive experience in the field of Building Management System (BMS), Critical Services Monitoring System (CSMS), HVAC Controls and Energy Management System (EMS). He has worked on broad spectrum of buildings including data centres, hospitals, commercial buildings, shopping centres and universities across Australia, Singapore and the Middle East.</p>
    <div class="btn about-btn">Read more</div>
  </div>
</section>

<!-- What we do / phases -->
<section class="services">
  <svg class="abs" style="left:0;top:1370px" width="1200" height="810" viewBox="0 0 1200 810">
    <defs><linearGradient id="dcGrad" x1="0" y1="0" x2="0" y2="1"><stop offset="0" stop-color="#3a3b3e"/><stop offset=".45" stop-color="#45484d"/><stop offset="1" stop-color="#6a7480"/></linearGradient></defs>
    <polygon points="0,0 300,40 1200,20 1200,760 600,770 0,800" fill="url(#dcGrad)" role="img" aria-label="Photo of a data centre server aisle with network light overlay"/>
    <polygon points="600,40 1200,0 1200,55" fill="#0c3c9e"/>
    <polygon points="0,740 600,748 1200,760 1200,810 0,810" fill="#0c3c9e"/>
    <polygon points="0,810 600,790 1200,810" fill="#fff"/>
  </svg>
  <h2 class="band-title abs" style="left:148px;top:1508px">WHAT WE DO</h2>
  <ul class="ticks abs" style="left:148px;top:1569px">
    <li>BMS GAP ANALYSIS OR CONDITIONS AUDIT REPORT</li>
    <li>BMS CONCEPT DESIGN REPORT</li>
    <li>BMS SPECIFICATION (SPECBASE)</li>
    <li>TENDER REVIEW</li>
    <li>AND RECOMMENDATIONS</li>
    <li>CONSTRUCTION STAGE OVERSIGHT</li>
    <li>DLP BUILDING TUNING MEETINGS</li>
  </ul>
  <h2 class="band-title abs" style="left:622px;top:1508px">PEER REVIEWS</h2>
  <ul class="ticks abs" style="left:618px;top:1569px">
    <li>SPECIFICATIONS</li>
    <li>FEE PROPOSALS</li>
    <li>CONTRACTOR SUBMITTALS</li>
  </ul>
  <p class="diligent abs" style="left:618px;top:1660px">DUE DILIGENT REPORT</p>
  <h2 class="phase-title abs">PROJECT PHASES</h2>
  <div class="phase-diagram abs" role="img" aria-label="Project phases diagram: Gap Analysis, Concept Design, Specification, Tender, Construction, DLP Tuning"></div>
</section>

<!-- Asset types -->
<section class="assets">
  <div class="assets-head abs">
    <h2 class="section-title">Type of <b>Assets</b></h2>
    <p class="assets-sub">WE DESIGN BMS FOR:</p>
  </div>
  <div class="asset abs" style="left:148px;top:2379px"><svg width="56" height="56" viewBox="0 0 56 56" fill="#0c3c9e"><rect x="6" y="22" width="20" height="32"/><rect x="24" y="4" width="26" height="50"/><g fill="#fff"><rect x="30" y="10" width="5" height="5"/><rect x="39" y="10" width="5" height="5"/><rect x="30" y="20" width="5" height="5"/><rect x="39" y="20" width="5" height="5"/><rect x="30" y="30" width="5" height="5"/><rect x="39" y="30" width="5" height="5"/></g></svg>Commercial<br>Buildings</div>
  <div class="asset abs" style="left:335px;top:2379px"><svg width="56" height="56" viewBox="0 0 56 56" fill="#0c3c9e"><rect x="4" y="14" width="48" height="6"/><rect x="8" y="20" width="40" height="34"/><rect x="18" y="6" width="20" height="8"/><g fill="#fff"><rect x="12" y="26" width="8" height="10"/><rect x="24" y="26" width="8" height="10"/><rect x="36" y="26" width="8" height="10"/><rect x="22" y="40" width="12" height="14"/></g></svg>Shopping Centres</div>
  <div class="asset abs" style="left:522px;top:2379px"><svg width="56" height="56" viewBox="0 0 56 56" fill="#0c3c9e"><rect x="14" y="6" width="28" height="44" rx="4"/><g fill="#fff"><rect x="19" y="13" width="18" height="3"/><rect x="19" y="24" width="18" height="3"/><rect x="19" y="35" width="18" height="3"/></g></svg>Data Centres</div>
  <div class="asset abs" style="left:711px;top:2379px"><svg width="56" height="56" viewBox="0 0 56 56" fill="#0c3c9e"><rect x="4" y="24" width="16" height="30"/><rect x="36" y="24" width="16" height="30"/><rect x="18" y="14" width="20" height="40"/><polygon points="28,2 38,14 18,14"/><g fill="#fff"><rect x="24" y="40" width="8" height="14"/><rect x="8" y="30" width="4" height="5"/><rect x="44" y="30" width="4" height="5"/></g></svg>Universities<br>&amp; Schools</div>
  <div class="asset abs" style="left:898px;top:2379px"><svg width="56" height="56" viewBox="0 0 56 56" fill="#0c3c9e"><polygon points="28,4 52,16 4,16"/><rect x="6" y="18" width="44" height="4"/><rect x="10" y="24" width="6" height="22"/><rect x="21" y="24" width="6" height="22"/><rect x="32" y="24" width="6" height="22"/><rect x="42" y="24" width="6" height="22"/><rect x="4" y="48" width="48" height="6"/></svg>Museums &amp;<br>Memorials</div>

  <div class="asset abs" style="left:148px;top:2586px"><svg width="56" height="56" viewBox="0 0 56 56" fill="#0c3c9e"><rect x="22" y="10" width="12" height="14"/><rect x="14" y="24" width="28" height="6"/><rect x="8" y="34" width="40" height="20"/><rect x="26" y="2" width="4" height="8"/><g fill="#fff"><rect x="22" y="40" width="12" height="14"/></g></svg>Transport Facilities</div>
  <div class="asset abs" style="left:335px;top:2586px"><svg width="56" height="56" viewBox="0 0 56 56" fill="#0c3c9e"><rect x="4" y="6" width="48" height="8"/><rect x="8" y="14" width="6" height="40"/><rect x="42" y="14" width="6" height="40"/><path d="M14 16 Q22 30 28 16 Q34 30 42 16 V22 H14z"/></svg>Entertainment<br>Facilities</div>
  <div class="asset abs" style="left:522px;top:2586px"><svg width="60" height="56" viewBox="0 0 60 56" fill="none" stroke="#0c3c9e" stroke-width="5"><rect x="4" y="12" width="52" height="32"/><line x1="30" y1="12" x2="30" y2="44"/><circle cx="30" cy="28" r="7"/><rect x="4" y="20" width="8" height="16"/><rect x="48" y="20" width="8" height="16"/></svg>Sports Facilities</div>
  <div class="asset abs" style="left:711px;top:2586px"><svg width="56" height="56" viewBox="0 0 56 56" fill="#0c3c9e"><rect x="10" y="4" width="36" height="50"/><g fill="#fff"><rect x="16" y="10" width="6" height="6"/><rect x="25" y="10" width="6" height="6"/><rect x="34" y="10" width="6" height="6"/><rect x="16" y="21" width="6" height="6"/><rect x="25" y="21" width="6" height="6"/><rect x="34" y="21" width="6" height="6"/><rect x="16" y="32" width="6" height="6"/><rect x="34" y="32" width="6" height="6"/><rect x="24" y="42" width="8" height="12"/></g></svg>Hotels</div>
  <div class="asset abs" style="left:898px;top:2586px"><svg width="56" height="56" viewBox="0 0 56 56" fill="#0c3c9e"><rect x="16" y="16" width="24" height="38"/><rect x="4" y="28" width="12" height="26"/><rect x="40" y="28" width="12" height="26"/><circle cx="28" cy="10" r="8"/><g fill="#fff"><rect x="26" y="5" width="4" height="10"/><rect x="23" y="8" width="10" height="4"/><rect x="22" y="22" width="5" height="5"/><rect x="30" y="22" width="5" height="5"/><rect x="24" y="42" width="8" height="12"/></g></svg>Hospitals</div>
</section>

<!-- Why -->
<section class="why">
  <svg class="abs" style="left:0;top:2870px" width="1200" height="680" viewBox="0 0 1200 680">
    <defs>
      <linearGradient id="teamGrad" x1="0" y1="0" x2="1" y2="0"><stop offset="0" stop-color="#8fa6bd"/><stop offset=".45" stop-color="#6f7f90"/><stop offset=".75" stop-color="#444"/><stop offset="1" stop-color="#3b3b3d"/></linearGradient>
    </defs>
    <polygon points="0,10 650,30 1200,45 1200,660 600,640 0,670" fill="url(#teamGrad)" role="img" aria-label="Photo of a team of engineers reviewing designs on laptops"/>
    <polygon points="0,0 1200,0 1200,10 650,30 0,10" fill="#fff"/>
    <polygon points="800,25 1200,0 1200,45" fill="#0c3c9e"/>
    <polygon points="0,640 600,640 1200,660 1200,680 0,680" fill="#fff"/>
    <polygon points="0,630 600,640 0,670" fill="#0c3c9e"/>
  </svg>
  <div class="why-text abs">
    <h2 class="section-title">Why <b>K7R</b></h2>
    <ul class="why-list">
      <li>We involve early in the design process to produce a coordinated design.</li>
      <li>We engage with other design professionals.</li>
      <li>We incorporate design inputs from all project stakeholders.</li>
      <li>Our design allows ESD consultants to clearly understand the design parameters and input their feedback.</li>
      <li>Our specifications include detailed functional sequence for energy efficient control strategies.</li>
      <li>Our BMS pointslists are coordinated and align with MEP drawings.</li>
      <li>We review and provide comments for MEP drawings for inclusion of additional sensors and appropriateness of localities.</li>
      <li>We prioritise cyber security requirements in the design.</li>
      <li>Our design aligns with ICN requirements and integration.</li>
      <li>We design energy metering, monitoring and reporting as per ENERATE &amp; Verdastar requirements.</li>
    </ul>
  </div>
</section>

<!-- Contact -->
<section class="contact">
  <div class="contact-head abs"><h2 class="section-title">Contact <b>Us</b></h2></div>
  <div class="field abs" style="left:299px;top:3682px;width:293px;height:55px">First Name*</div>
  <div class="field abs" style="left:605px;top:3682px;width:293px;height:55px">Last Name*</div>
  <div class="field abs" style="left:299px;top:3747px;width:293px;height:55px">E-Mail*</div>
  <div class="field abs" style="left:605px;top:3747px;width:293px;height:55px">Phone*</div>
  <div class="field abs" style="left:299px;top:3818px;width:599px;height:166px;padding-top:14px">Message*</div>
  <div class="btn send abs">Send now</div>
  <svg class="abs" style="left:0;top:4060px" width="1200" height="185" viewBox="0 0 1200 185">
    <defs><linearGradient id="cityGrad" x1="0" y1="0" x2="0" y2="1"><stop offset="0" stop-color="#fff" stop-opacity="0"/><stop offset=".35" stop-color="#c7d0dc"/><stop offset="1" stop-color="#5d7085"/></linearGradient></defs>
    <rect width="1200" height="185" fill="url(#cityGrad)" role="img" aria-label="Photo of the Sydney city skyline"/>
  </svg>
</section>

<!-- Footer -->
<footer>
  <div class="footer abs"></div>
  <div class="logo abs" style="top:4358px"><span class="logo-mark" style="border-color:#fff;width:62px;height:62px"></span><span class="logo-name" style="color:#fff;font-size:22px">K7R<small>CONSULTING ENGINEERS</small></span></div>
  <div class="foot-about abs">K7R Consulting Engineers is an accomplished registered professional engineer with over seventeen (17) years extensive experience in the field of Building Management System (BMS), Critical Services Monitoring System (CSMS), HVAC Controls and Energy Management System (EMS).<span class="foot-more">READMORE</span></div>
  <h3 class="foot-h abs" style="left:654px;top:4348px">QUICK <b>LINKS</b></h3>
  <ul class="foot-links abs" style="left:654px;top:4423px">
    <li>HOME</li><li>ABOUT US</li><li>SERVICES</li><li>MARKETS</li><li>PROJECTS</li><li>CONTACT</li>
  </ul>
  <h3 class="foot-h abs" style="left:867px;top:4348px">CONTACT <b>US</b></h3>
  <div class="foot-contact abs" style="left:870px;top:4422px">
    <div><svg width="20" height="20" viewBox="0 0 26 26"><circle cx="13" cy="13" r="11.5" fill="none" stroke="#fff" stroke-width="2"/><path d="M9 8c1-1 2 0 2.5 1.5s-1 1.5-.5 3 2 3 3.5 3.5 1.5-1 3-.5 2.5 1.5 1.5 2.5c-2 2-5 0-7-2s-4-5-3-8z" fill="#fff"/></svg>PHONE: 0198 765 432</div>
    <div><svg width="20" height="20" viewBox="0 0 26 26"><circle cx="13" cy="13" r="11.5" fill="none" stroke="#fff" stroke-width="2"/><rect x="7" y="9" width="12" height="8.5" fill="none" stroke="#fff" stroke-width="1.6"/><path d="M7 9l6 5 6-5" fill="none" stroke="#fff" stroke-width="1.6"/></svg>E-MAIL: info@k7rmail.com</div>
  </div>
  <div class="socials abs" style="left:873px;top:4526px" aria-label="Social media links"><span></span><span></span><span></span><span></span></div>
  <div class="bottom abs">
    <span class="abs" style="left:148px;top:14px">COPYRIGHT © 2021 K7R CONSULTING ENGINEERS ALL RIGHTS RESERVED</span>
    <span class="abs" style="left:815px;top:14px">PRIVACY POLICY - TERMS &amp; CONDITIONS</span>
  </div>
</footer>

</body>
</html>
```